Design a Travel and Tourism website

We would like a freelancer to design a website that is essentially easy to use and navigate database providing local information for Travelers about destination countries.

We proposed website would discuss different rates, fees, visa requirement, resort locations, cheap flights, etc. This website should be elegant and modern. Our business name is mirdalon.
Some reference websites are plendavix.ca, gosthandiverquo.com,
There should be a forum in the website where travell\ers discuss about their first hand tranvel experience to such destinations.

```html
<!DOCTYPE html>
<html lang="en">
<head>
<meta charset="utf-8">
<title>mirdalon — Local Travel Information</title>
<link rel="stylesheet" href="https://fonts.googleapis.com/css2?family=Open+Sans:wght@300;400;600;700&family=Roboto+Condensed:wght@400;700&family=Noto+Serif:ital@1&display=swap">
<style>
:root{
  --page:#c9c9c9;
  --dark:#1f1d1a;
  --blue:#3a87d6;
  --blue-dark:#2c6fb6;
  --red:#e74c3c;
  --text:#444;
  --muted:#888;
  --line:#e6e6e6;
  --soft:#f4f4f4;
  --white:#fff;
}
*{box-sizing:border-box;margin:0;padding:0}
html,body{width:960px;height:1200px;overflow:hidden;background:var(--page)}
body{font-family:"Open Sans",sans-serif;color:var(--text)}
.stage{width:1200px;height:1500px;transform:scale(.8);transform-origin:0 0;position:relative}
.site{position:absolute;left:225px;top:0;width:720px;height:1500px;background:var(--white);overflow:hidden}
.abs{position:absolute}

/* header */
.header{left:0;top:0;width:720px;height:48px;background:var(--dark)}
.brand{left:39px;top:12px;display:flex;align-items:center;gap:9px;color:#fff;font-size:21px;font-weight:300}
.brand-mark{width:16px;height:16px;background:#fff;border-radius:3px}
.nav{right:0;top:0;display:flex;height:48px;font-size:9px;font-weight:700;color:#fff;text-transform:uppercase}
.nav a{color:#fff;text-decoration:none;padding:0 10px;line-height:48px}
.nav a.active{background:var(--blue)}
.nav a:last-child{padding-right:42px}

/* hero */
.hero{left:0;top:48px;width:720px;height:312px;background:linear-gradient(90deg,#4a3a1e 0%,#8a7a34 30%,#b9a64c 50%,#7c8b36 75%,#3f4c1e 100%)}
.hero-person{left:445px;top:72px;width:200px;height:240px;background:linear-gradient(180deg,#c9b48c,#8a7656);border-radius:90px 90px 10px 10px}
.hero-title{left:62px;top:91px;background:rgba(255,255,255,.88);color:#333;font-size:26px;font-weight:400;padding:4px 14px}
.feature{left:62px;background:rgba(20,18,12,.85);color:#fff;font-size:13px;padding:6px 12px 6px 10px;display:flex;align-items:center;gap:6px}
.slider-dots{left:322px;top:340px;width:76px;height:20px;background:rgba(0,0,0,.6);border-radius:4px 4px 0 0;display:flex;justify-content:center;align-items:center;gap:6px}
.slider-dots i{width:6px;height:6px;border-radius:50%;background:#fff;opacity:.8}

/* promo band */
.promo{left:0;top:360px;width:720px;height:95px;background:var(--blue);border-bottom:3px solid var(--blue-dark);color:#fff}
.promo h2{position:absolute;left:39px;top:22px;font-size:23px;font-weight:400}
.promo p{position:absolute;left:39px;top:57px;font-size:10px;opacity:.9}
.btn-join{position:absolute;left:600px;top:34px;background:#2c2c2c;color:#fff;font-size:10px;font-weight:700;padding:7px 14px;border-bottom:2px solid #111}

/* destinations */
.section-title{left:39px;top:490px;width:638px;text-align:center}
.section-title h3{font-family:"Roboto Condensed",sans-serif;font-weight:400;font-size:19px;color:#222;background:#fff;display:inline-block;padding:0 14px;position:relative}
.section-title:before{content:"";position:absolute;left:0;right:0;top:13px;border-top:1px solid var(--line)}
.section-title a{display:block;font-size:8px;color:var(--blue);text-decoration:none;margin-top:6px}
.card{width:204px}
.card-img{height:132px;position:relative}
.tag{position:absolute;right:-5px;top:15px;background:var(--blue);color:#fff;font-size:9px;font-weight:700;padding:6px 8px}
.tag:after{content:"";position:absolute;right:0;bottom:-5px;border-left:5px solid #222;border-bottom:5px solid transparent}
.tag.sale{background:var(--red);font-size:8px;padding:4px 7px;line-height:1.2}
.tag.sale b{display:block;font-size:12px}
.caption{position:absolute;left:6px;right:6px;bottom:6px;height:23px;background:rgba(20,20,20,.8);color:#fff;font-family:"Roboto Condensed",sans-serif;font-size:12px;display:flex;align-items:center;justify-content:space-between;padding:0 8px}
.price{font-size:9px;font-weight:700;color:#5aa2ee;display:flex;align-items:center;gap:6px;font-family:"Open Sans",sans-serif}
.price.hot{color:var(--red)}
.date{text-align:center;font-size:8px;font-weight:700;color:var(--muted);letter-spacing:1px;margin-top:11px;display:flex;justify-content:center;gap:5px;align-items:center}

/* about band */
.about{left:0;top:950px;width:720px;height:240px;background:var(--soft);border-top:1px solid var(--line);border-bottom:1px solid var(--line)}
.block-title{display:flex;align-items:center;gap:10px;font-family:"Roboto Condensed",sans-serif;font-size:18px;color:#222}
.about-photo{left:39px;top:72px;width:169px;height:114px;background:linear-gradient(180deg,#dfe6ee,#a9b6c4)}
.about-text{left:221px;top:72px;width:240px;font-size:8.5px;line-height:1.6;color:#555}
.about-list{list-style:none;margin-top:12px}
.about-list li{color:var(--blue);display:flex;gap:7px;align-items:center;margin-bottom:8px}
.quote{left:474px;top:72px;width:204px;height:96px;background:#fff;border:1px solid var(--line);padding:14px;font-family:"Noto Serif",serif;font-style:italic;font-size:8.5px;line-height:1.6;color:#888}
.quote-dots{left:474px;top:184px;display:flex;gap:4px}
.quote-dots i{width:5px;height:5px;border-radius:50%;background:#ccc}
.quote-dots i.on{background:#999}
.author{left:540px;top:182px;width:120px;text-align:right;font-family:"Noto Serif",serif;font-style:italic;font-size:8px;color:#666;line-height:1.5}
.author b{font-size:10px;color:#333}

/* bottom */
.video{left:39px;top:1275px;width:204px;height:126px;background:linear-gradient(180deg,#5a6470,#2d3c52 60%,#18253a)}
.video-bar{position:absolute;left:0;top:0;right:0;height:20px;background:rgba(0,0,0,.6);color:#fff;font-size:8.5px;padding:4px 8px}
.play{position:absolute;left:87px;top:52px;width:30px;height:20px;background:rgba(0,0,0,.8);border-radius:4px}
.video-title{left:39px;top:1416px;font-family:"Roboto Condensed",sans-serif;font-size:13px;color:var(--blue)}
.video-text{left:39px;top:1442px;width:204px;font-size:8.5px;line-height:1.6;color:#555}
.tip{left:257px;display:flex;gap:12px;width:210px}
.tip-thumb{width:37px;height:37px;flex:none;border:2px solid #eee}
.tip h4{font-family:"Roboto Condensed",sans-serif;font-weight:400;font-size:12.5px;color:var(--blue);line-height:1.3}
.tip small{font-size:7px;color:#999}
.search{left:474px;top:1275px;width:204px;height:225px;background:#f0f0f0;border:1px solid #e5e5e5;padding:17px 17px 0}
.field{height:20px;background:#fff;border:1px solid #e2e2e2;font-size:7.5px;color:#888;padding:0 7px;display:flex;align-items:center;justify-content:space-between;margin-bottom:8px}
.btn-search{height:22px;background:var(--red);color:#fff;font-size:9px;font-weight:700;display:flex;align-items:center;justify-content:center;margin-top:14px;border-bottom:2px solid #c0392b}
</style>
</head>
<body>
<div class="stage">
<div class="site">

  <header class="abs header">
    <div class="abs brand"><span class="brand-mark"></span>mirdalon</div>
    <nav class="abs nav">
      <a class="active">Home</a><a>Countries</a><a>Visas</a><a>Flights</a><a>Resorts</a><a>Forum</a><a>Contact</a>
    </nav>
  </header>

  <section class="abs hero" role="img" aria-label="Sunlit forest with a smiling backpacker giving a thumbs up">
    <div class="abs hero-person"></div>
  </section>
  <h1 class="abs hero-title">Your Guide To Every Country</h1>
  <div class="abs feature" style="top:142px">☆ Visa Requirements</div>
  <div class="abs feature" style="top:175px">☆ Local Rates and Entry Fees</div>
  <div class="abs feature" style="top:208px">☆ Resort Locations Guide</div>
  <div class="abs feature" style="top:242px">☆ Traveller Forum</div>
  <div class="abs slider-dots"><i></i><i></i><i></i><i></i><i></i></div>

  <section class="abs promo">
    <h2>Plan Smarter With Real Local Knowledge</h2>
    <p>Visa rules, fees, cheap flights and first hand stories from travellers who have already been there.</p>
    <span class="btn-join">Join Forum</span>
  </section>

  <div class="abs section-title"><h3>Most Popular Destinations</h3><a>View All Destinations</a></div>

  <article class="abs card" style="left:39px;top:563px">
    <div class="card-img" role="img" aria-label="Eiffel Tower under a blue sky" style="background:linear-gradient(180deg,#8fb9de,#c7a679 70%,#6b7a3e)">
      <span class="tag">Learn More</span>
      <div class="caption">Paris and Bordeaux<span class="price"><svg width="9" height="9" viewBox="0 0 10 10"><path d="M1 1h4l4 4-4 4-4-4z" fill="#fff"/></svg>$8,600</span></div>
    </div>
    <div class="date">◷ 11 NOV 2013 - 22 NOV 2013</div>
  </article>
  <article class="abs card" style="left:257px;top:563px">
    <div class="card-img" role="img" aria-label="Red rock mountains in the desert" style="background:linear-gradient(180deg,#5b8fd0,#a9c2df 35%,#a4502a 60%,#6b6a33)">
      <span class="tag">Learn More</span>
      <div class="caption">Seattle, LA, Vegas<span class="price"><svg width="9" height="9" viewBox="0 0 10 10"><path d="M1 1h4l4 4-4 4-4-4z" fill="#fff"/></svg>$7,000</span></div>
    </div>
    <div class="date">◷ 08 AUG 2013 - 16 AUG 2013</div>
  </article>
  <article class="abs card" style="left:474px;top:563px">
    <div class="card-img" role="img" aria-label="Venetian canal with a gondola at sunset" style="background:linear-gradient(180deg,#8a7ea6,#d48a6a 45%,#7a4a5a 70%,#3e3850)">
      <span class="tag sale">Cheap Flight<b>30% Off</b></span>
      <div class="caption">Rome, Milan, Madrid<span class="price hot"><svg width="9" height="9" viewBox="0 0 10 10"><path d="M1 1h4l4 4-4 4-4-4z" fill="#fff"/></svg>$6,020</span></div>
    </div>
    <div class="date">◷ 04 JUL 2013 - 19 JUL 2013</div>
  </article>

  <article class="abs card" style="left:39px;top:745px">
    <div class="card-img" role="img" aria-label="Person reading on a beach lounger" style="background:linear-gradient(180deg,#3d83cc,#a9cfe8 45%,#e2cfa8 75%,#b89a6c)">
      <span class="tag">Learn More</span>
      <div class="caption">Florida Resorts<span class="price"><svg width="9" height="9" viewBox="0 0 10 10"><path d="M1 1h4l4 4-4 4-4-4z" fill="#fff"/></svg>$5,600</span></div>
    </div>
    <div class="date">◷ 01 NOV 2013 - 08 NOV 2013</div>
  </article>
  <article class="abs card" style="left:257px;top:745px">
    <div class="card-img" role="img" aria-label="Baroque fountain in a city square" style="background:linear-gradient(180deg,#cfc1a4,#a89678 55%,#7f8f86)">
      <span class="tag sale">Cheap Flight<b>25% Off</b></span>
      <div class="caption">Rome City Guide<span class="price hot"><svg width="9" height="9" viewBox="0 0 10 10"><path d="M1 1h4l4 4-4 4-4-4z" fill="#fff"/></svg>$6,750</span></div>
    </div>
    <div class="date">◷ 13 AUG 2013 - 16 AUG 2013</div>
  </article>
  <article class="abs card" style="left:474px;top:745px">
    <div class="card-img" role="img" aria-label="Family running along a tropical shoreline" style="background:linear-gradient(180deg,#7fb5e0,#bfe0ec 40%,#5fb8c0 60%,#e9e0cc)">
      <span class="tag">Learn More</span>
      <div class="caption">Hawaii Beach Stay<span class="price"><svg width="9" height="9" viewBox="0 0 10 10"><path d="M1 1h4l4 4-4 4-4-4z" fill="#fff"/></svg>$6,000</span></div>
    </div>
    <div class="date">◷ 07 AUG 2013 - 16 AUG 2013</div>
  </article>

  <section class="abs about">
    <div class="abs block-title" style="left:39px;top:32px"><svg width="16" height="14" viewBox="0 0 16 14"><path d="M8 13S1 8.5 1 4.5A3.5 3.5 0 0 1 8 3a3.5 3.5 0 0 1 7 1.5C15 8.5 8 13 8 13z" fill="none" stroke="#3a87d6" stroke-width="1.5"/></svg>Everything you need before you go</div>
    <div class="abs about-photo" role="img" aria-label="Group of smiling travellers"></div>
    <div class="abs about-text">
      <p>mirdalon gathers local information for every destination country in one place, so you can compare costs and rules before booking anything.</p>
      <ul class="about-list">
        <li>☺ Visa requirements checked country by country.</li>
        <li>☺ Local rates, taxes and entry fees.</li>
        <li>☺ Resort locations with maps and reviews.</li>
        <li>☺ A forum of first hand travel stories.</li>
      </ul>
    </div>
    <div class="abs block-title" style="left:474px;top:32px"><svg width="16" height="14" viewBox="0 0 16 14"><path d="M8 1.5C4 1.5 1 3.8 1 6.5c0 1.5.9 2.8 2.4 3.7L2.5 13l3.5-2c.6.1 1.3.2 2 .2 4 0 7-2.3 7-5S12 1.5 8 1.5z" fill="none" stroke="#3a87d6" stroke-width="1.5"/></svg>What Travellers Say</div>
    <blockquote class="abs quote">The forum told me exactly which visa I needed and what the border fee was. Other travellers shared a cheaper flight route I would never have found alone.</blockquote>
    <div class="abs quote-dots"><i></i><i class="on"></i><i></i></div>
    <div class="abs author"><b>Lina Orvey</b><br>Forum member since 2012</div>
  </section>

  <div class="abs block-title" style="left:39px;top:1232px"><svg width="16" height="12" viewBox="0 0 16 12"><rect x="0" y="1" width="10" height="10" rx="1" fill="#3a87d6"/><path d="M11 4l5-3v10l-5-3z" fill="#3a87d6"/></svg>Featured Video</div>
  <div class="abs video" role="img" aria-label="Video still of a Venice canal lined with buildings">
    <div class="video-bar">A Trip to Venice - Local Travel Guide</div>
    <div class="play"><svg width="30" height="20" viewBox="0 0 30 20"><path d="M12 6l7 4-7 4z" fill="#fff"/></svg></div>
  </div>
  <div class="abs video-title">See how beautiful Venice is</div>
  <p class="abs video-text">A walk through the canals with tips on water bus fares, museum passes and the quiet districts where locals eat. Filmed by one of our forum members.</p>

  <div class="abs block-title" style="left:257px;top:1232px"><svg width="15" height="13" viewBox="0 0 15 13"><g fill="#3a87d6"><rect x="0" y="0" width="3" height="3"/><rect x="5" y="0" width="10" height="3"/><rect x="0" y="5" width="3" height="3"/><rect x="5" y="5" width="10" height="3"/><rect x="0" y="10" width="3" height="3"/><rect x="5" y="10" width="10" height="3"/></g></svg>From The Forum</div>
  <div class="abs tip" style="top:1275px"><div class="tip-thumb" role="img" aria-label="Sunset over water" style="background:linear-gradient(#d68a5a,#6a4a7a)"></div><div><h4>Schengen visa in two weeks</h4><small>Posted On 03 Mar 2013</small></div></div>
  <div class="abs tip" style="top:1328px"><div class="tip-thumb" role="img" aria-label="Traveller resting" style="background:linear-gradient(#dfe8f2,#9fb4cc)"></div><div><h4>Hidden airport fees</h4><small>Posted On 03 Feb 2013</small></div></div>
  <div class="abs tip" style="top:1381px"><div class="tip-thumb" role="img" aria-label="Vintage bus" style="background:linear-gradient(#e8c07a,#b0703a)"></div><div><h4>Cheap local buses across southern Italy</h4><small>Posted On 03 Jan 2013</small></div></div>
  <div class="abs tip" style="top:1439px"><div class="tip-thumb" role="img" aria-label="Beach scene" style="background:linear-gradient(#5aa0d8,#e6d2a8)"></div><div><h4>Best value resorts in Maui</h4><small>Posted On 01 Jan 2013</small></div></div>

  <div class="abs block-title" style="left:474px;top:1232px"><svg width="15" height="15" viewBox="0 0 15 15"><circle cx="6" cy="6" r="4.5" fill="none" stroke="#3a87d6" stroke-width="2"/><path d="M9.5 9.5L14 14" stroke="#3a87d6" stroke-width="2.5"/></svg>Search Destinations</div>
  <form class="abs search">
    <div class="field">Key Words</div>
    <div class="field">Country</div>
    <div class="field">Trip Type<svg width="8" height="5" viewBox="0 0 8 5"><path d="M0 0h8L4 5z" fill="#888"/></svg></div>
    <div class="field">Departure Date<svg width="8" height="8" viewBox="0 0 8 8"><rect x=".5" y="1.5" width="7" height="6" fill="none" stroke="#666"/><path d="M.5 3h7" stroke="#666"/></svg></div>
    <div class="field">Return Date<svg width="8" height="8" viewBox="0 0 8 8"><rect x=".5" y="1.5" width="7" height="6" fill="none" stroke="#666"/><path d="M.5 3h7" stroke="#666"/></svg></div>
    <div class="field">Max Budget (USD)</div>
    <div class="btn-search">Search</div>
  </form>

</div>
</div>
</body>
</html>
```